Vértice Solar needs the best stationery in the development business

We need a stationary design for a new company based in Porto, Portugal. We are a new property development management company specialized in downtown regeneration projects and adaptive use of old big textile factories.

We just have selected our new logo in a pixelbazaar competition and now we are searching for the best stationary design. We expect to receive proposals for:

Two sided business cards
A4 main letterhead
A4 simple text papper
A4 and A5 envelops
A4 single folder front page

information for the stationary project

company signature: FormaCrescimentoDireção (as in the logo files attached)

Business card information: 
Tomás Vieira Lobato FRICS
Managing Director

email: tomas@verticesolar-exemplo.pt
website: www.verticesolar-exemplo.pt

adress: 
R. das Camélias, 83 - 2º
4050-217 Porto

office number
+(351) 22 418 76 53
fax number
+(351) 22 418 76 59
mobile
+(351) 934 207 615

Target Market(s)

professional finantial fund managers and big property owners

Industry/Entity Type

Business

Requirements
Must have
• the company logo

Nice to have
• clear simple contemporary design is appreciated

```html
<!DOCTYPE html>
<html lang="pt">
<head>
<meta charset="utf-8">
<title>Vértice Solar — Business Card</title>
<link rel="stylesheet" href="https://fonts.googleapis.com/css2?family=PT+Sans:wght@400;700&display=swap">
<style>
  :root {
    --page-bg: #ffffff;
    --card-bg: #ffffff;
    --card-edge: #b9b9b9;
    --brand-blue: #2c5eb3;
    --brand-blue-light: #6f93d6;
    --text-dark: #3f3f3f;
    --text-body: #333333;
  }
  * { margin: 0; padding: 0; box-sizing: border-box; }
  html, body {
    width: 1200px;
    height: 900px;
    overflow: hidden;
    background: var(--page-bg);
  }
  .sheet {
    position: relative;
    width: 1200px;
    height: 900px;
    font-family: "PT Sans", Arial, sans-serif;
  }
  .card {
    position: absolute;
    left: 268px;
    width: 680px;
    background: var(--card-bg);
    border: 1.5px solid var(--card-edge);
    overflow: hidden;
  }
  .card--front { top: 44px; height: 390px; }
  .card--back  { top: 488px; height: 392px; }

  .brand {
    position: absolute;
    left: 320px;
    top: 30px;
    width: 290px;
    text-align: center;
  }
  .brand__dot {
    display: block;
    width: 44px;
    height: 44px;
    margin: 0 auto 6px;
    border-radius: 50%;
    background: var(--brand-blue);
  }
  .brand__name {
    font-size: 36px;
    font-weight: 700;
    color: var(--brand-blue);
    letter-spacing: -0.5px;
    line-height: 1;
  }

  .holder {
    position: absolute;
    left: 318px;
    top: 184px;
    color: var(--text-dark);
  }
  .holder__name {
    font-size: 20px;
    font-weight: 700;
    line-height: 28px;
  }
  .holder__role {
    font-size: 18px;
    line-height: 26px;
  }
  .holder__links {
    margin-top: 32px;
    font-size: 18px;
    line-height: 26px;
  }

  .brand-field {
    position: absolute;
    left: 0;
    top: 46px;
    width: 284px;
    height: 346px;
  }

  .contact {
    position: absolute;
    left: 444px;
    top: 86px;
    color: var(--text-body);
    font-size: 18px;
    line-height: 27px;
  }
  .contact__address { margin-bottom: 20px; }
</style>
</head>
<body>
<main class="sheet">

  <section class="card card--front" aria-label="Business card, front">
    <div class="brand">
      <span class="brand__dot"></span>
      <div class="brand__name">Vértice Solar</div>
    </div>
    <div class="holder">
      <p class="holder__name">Tomás Vieira Lobato FRICS</p>
      <p class="holder__role">Managing Director</p>
      <div class="holder__links">
        <p>tomas@verticesolar-exemplo.pt</p>
        <p>www.verticesolar-exemplo.pt</p>
      </div>
    </div>
  </section>

  <section class="card card--back" aria-label="Business card, back">
    <svg class="brand-field" viewBox="0 0 284 346" role="img" aria-label="Large brand symbol in blue">
      <defs>
        <radialGradient id="brandFieldTone" cx="0.45" cy="0.35" r="0.75">
          <stop offset="0" stop-color="var(--brand-blue-light)"/>
          <stop offset="1" stop-color="var(--brand-blue)"/>
        </radialGradient>
      </defs>
      <circle cx="110" cy="180" r="172" fill="url(#brandFieldTone)"/>
    </svg>
    <div class="contact">
      <p class="contact__address">R. das Camélias, 83 - 2º<br>4050-217 Porto</p>
      <p>office number<br>+(351) 22 418 76 53<br>fax number<br>+(351) 22 418 76 59<br>mobile<br>+(351) 934 207 615</p>
    </div>
  </section>

</main>
</body>
</html>
```